Ranked amongst the Best Colleges and Programs

the size of the ad is Full Page, with bleed*
8”x 10.75" plus 0.25" bleed'
you have two choices for the tagline .. please chose what ever you think will allow you to make a better ad.
The instructions on the brief are in red
I am looking for a hight quality modern ad to place in local weekly publications that will stand out .
I would like a ad that people will look at and say i would like to see what this ad is all about.
I apprecate creative work.
the ad should not be very crowded and the text should be able to be read.
if you decide to use people in the ad .. (you don't have to ) then it should be a male dressed in white shirt in and sports jacket.. or if you would like you can use a vector and then use male or female people.
please leave one inch on the bottom for the footer

Target Market(s)

potential middle class students from 23-35 years of age

Industry/Entity Type

education

Requirements
Must have
• .the " 98% employment rate" should stand out in the ad.. but should not be the main part of the ad
Nice to have
• creative
Should not have
• Should not be a very busy or crowded ad.. i prefer pictures of men but should be .. in a business suit .. that looks professional- white shirt

```html
<!DOCTYPE html>
<html lang="en">
<head>
<meta charset="utf-8">
<title>Masters of Accounting – Full Page Ad</title>
<link href="https://fonts.googleapis.com/css2?family=Poppins:wght@300;400;500&family=Oswald:wght@200&display=swap" rel="stylesheet">
<style>
  :root{
    --stage:#cdcdcd;
    --ink-dark:#2a2a2a;
    --teal:#72b3c0;
    --white:#ffffff;
    --text:#1e1e1e;
    --rule:#8a8a8a;
  }
  *{margin:0;padding:0;box-sizing:border-box}
  html,body{width:1200px;height:675px;overflow:hidden}
  body{background:var(--stage);font-family:'Poppins',sans-serif;position:relative}

  .sample-label{
    position:absolute;top:58px;
    writing-mode:vertical-rl;transform:rotate(180deg);
    font-weight:300;font-size:22px;color:#111;
  }
  .sample-label.one{left:32px}
  .sample-label.two{left:672px}

  .ad{position:absolute;top:54px;width:423px;height:564px;background:var(--white);overflow:hidden}
  .ad.one{left:75px}
  .ad.two{left:714px}

  .ad-hero{position:absolute;left:0;top:0;width:423px;height:443px;background:var(--ink-dark)}
  .ad.one .ad-hero{background:linear-gradient(90deg,#3a3a3a 0%,#2c2c2c 45%,#242424 100%)}
  .ad.two .ad-hero{background:linear-gradient(180deg,#2a2a2a 0%,#1f1f1f 100%)}

  .portrait{position:absolute;top:80px;height:363px}
  .ad.one .portrait{left:0;width:225px;
    background:linear-gradient(180deg,rgba(90,80,72,.55) 0%,rgba(150,150,152,.55) 45%,rgba(120,120,124,.6) 100%);
    border-radius:90px 90px 0 0}
  .ad.two .portrait{left:0;width:260px;
    background:linear-gradient(180deg,rgba(110,85,70,.5) 0%,rgba(40,52,80,.8) 45%,rgba(28,36,58,.9) 100%);
    border-radius:100px 100px 0 0}

  .headline{position:absolute;left:0;right:0;top:15px;text-align:center;color:var(--white)}
  .headline .line-small{display:block;font-size:19.5px;font-weight:400;letter-spacing:.3px;line-height:1.3}
  .headline .line-large{display:block;font-size:27px;font-weight:500;letter-spacing:.2px;line-height:1.2}

  .rankings{position:absolute;right:23px;top:268px;text-align:right;color:var(--white)}
  .rankings .school{font-size:12px;font-weight:400;line-height:1.2}
  .rankings .program{font-size:13.4px;font-weight:500;color:var(--teal);line-height:1.3}
  .rankings .intro{font-size:11px;font-weight:400;margin-top:8px}
  .rankings .rule{height:1px;width:48px;background:var(--rule);margin:7px 0 6px auto}
  .rankings .award{font-size:13.4px;font-weight:500;color:var(--teal);line-height:1.3}
  .rankings .source{font-size:11px;font-weight:400;line-height:1.45}

  .stat-box{position:absolute;left:24px;top:411px;width:92px;height:81px;background:var(--teal);color:var(--white);text-align:center}
  .stat-box .figure{display:block;font-family:'Oswald',sans-serif;font-weight:200;font-size:62px;line-height:1;margin-top:2px;letter-spacing:-1px;transform:scaleX(.8)}
  .stat-box .label{display:block;font-size:8.2px;font-weight:300;letter-spacing:.1px;margin-top:2px}

  .stat-copy{position:absolute;left:130px;top:454px;width:261px;font-size:8.6px;line-height:1.22;color:var(--text);text-align:justify}
</style>
</head>
<body>

  <div class="sample-label one">Sample 1</div>
  <div class="sample-label two">Sample 2</div>

  <article class="ad one">
    <div class="ad-hero">
      <div class="portrait" role="img" aria-label="Photo of a smiling man in glasses wearing a grey sports jacket, white shirt and tie, holding a tablet in an office"></div>
      <h1 class="headline">
        <span class="line-small">A small &nbsp;investment Today,</span>
        <span class="line-large">a big difference Tomorrow</span>
      </h1>
      <div class="rankings">
        <div class="school">ZVU–</div>
        <div class="program">Masters of Accounting</div>
        <div class="intro">Ranked amongst</div>
        <div class="rule"></div>
        <div class="award">Best Colleges</div>
        <div class="source">Calvor 2023</div>
        <div class="rule"></div>
        <div class="award">Best Masters in Accounting</div>
        <div class="source">Studiora 2023</div>
      </div>
    </div>
    <div class="stat-box">
      <span class="figure">98%</span>
      <span class="label">EMPLOYMENT RATE</span>
    </div>
    <p class="stat-copy">ZVS graduates have gone on to work in high-quality jobs in top firms, earning impressive six-figure salaries as well as opening successful businesses.</p>
  </article>

  <article class="ad two">
    <div class="ad-hero">
      <div class="portrait" role="img" aria-label="Photo of a smiling bearded man in a navy suit, white shirt and black tie"></div>
      <h1 class="headline">
        <span class="line-small">A small &nbsp;investment Today,</span>
        <span class="line-large">a big difference Tomorrow</span>
      </h1>
      <div class="rankings">
        <div class="school">ZVU–</div>
        <div class="program">Masters of Accounting</div>
        <div class="intro">Ranked amongst</div>
        <div class="rule"></div>
        <div class="award">Best Colleges</div>
        <div class="source">Calvor 2023</div>
        <div class="rule"></div>
        <div class="award">Best Masters in Accounting</div>
        <div class="source">Studiora 2023</div>
      </div>
    </div>
    <div class="stat-box">
      <span class="figure">98%</span>
      <span class="label">EMPLOYMENT RATE</span>
    </div>
    <p class="stat-copy">ZVS graduates have gone on to work in high-quality jobs in top firms, earning impressive six-figure salaries as well as opening successful businesses.</p>
  </article>

</body>
</html>
```